Trendy, rustic, patriotic Facebook Design!

Would like something to catch people's eye! Must include our logo and phone number. 410-587-3920. Dogs in the project are a must. Bold pricing, location, etc to catch peoples eyes is a plus.

Target Market(s)

Dog owners

Font styles to use
Serif
Sans Serif

Colors
1f66ae
ec1f27
ffffff

Requirements
Must have
• Dogs, company logo, business phone 410-587-3920 and website www.furlowpaws.com
Nice to have
• Something that is rustic, trendy!
Should not have
• Cartoons.

```html
<!DOCTYPE html>
<html lang="en">
<head>
<meta charset="utf-8">
<title>Furlow Paws – Cover Concepts</title>
<link rel="stylesheet" href="https://fonts.googleapis.com/css2?family=Bebas+Neue&family=Montserrat:ital,wght@0,400;0,800;1,700&display=swap">
<style>
  :root {
    --board: #1c1c1c;
    --label: #4a4a4a;
    --navy: #14306b;
    --red: #d2152a;
    --white: #ffffff;
    --paper: #f4f4f4;
  }
  html, body {
    margin: 0;
    width: 1006px;
    height: 1200px;
    overflow: hidden;
    background: var(--board);
  }
  .board {
    position: relative;
    width: 1006px;
    height: 1200px;
    font-family: "Montserrat", sans-serif;
  }
  .board-title {
    position: absolute;
    top: 72px;
    left: 0;
    width: 1006px;
    margin: 0;
    text-align: center;
    color: var(--white);
    font-style: italic;
    font-weight: 700;
    font-size: 22px;
    letter-spacing: 2px;
  }
  .sample-label, .sample-size {
    position: absolute;
    margin: 0;
    color: var(--label);
    font-weight: 400;
    font-size: 33px;
    letter-spacing: 1px;
  }
  .sample-label { left: 50px; }
  .sample-size { right: 50px; }
  .cover {
    position: absolute;
    left: 186px;
    width: 635px;
    height: 242px;
    display: block;
  }
  .headline-top { font-family: "Bebas Neue", sans-serif; fill: var(--navy); font-size: 38px; }
  .headline-main { font-family: "Bebas Neue", sans-serif; fill: var(--red); font-size: 48px; }
  .brand-name { font-family: "Bebas Neue", sans-serif; fill: var(--navy); font-size: 22px; letter-spacing: 1px; }
  .band-offer { font-family: "Montserrat", sans-serif; font-weight: 800; fill: var(--white); font-size: 13px; letter-spacing: 1.5px; }
  .band-phone { font-family: "Montserrat", sans-serif; font-weight: 800; fill: var(--white); font-size: 22px; }
  .band-web { font-family: "Montserrat", sans-serif; font-weight: 800; fill: var(--white); font-size: 15px; }
</style>
</head>
<body>
<main class="board">
  <h1 class="board-title">TRENDY, RUSTIC, PATRIOTIC FACEBOOK DESIGN!</h1>

  <p class="sample-label" style="top:160px;">SAMPLE 1</p>
  <p class="sample-size" style="top:160px;">820X312</p>

  <svg class="cover" style="top:260px;" viewBox="0 0 635 242" xmlns="http://www.w3.org/2000/svg">
    <defs>
      <linearGradient id="paper1" x1="0" y1="0" x2="1" y2="1">
        <stop offset="0" stop-color="#e9e9e9"/>
        <stop offset="0.5" stop-color="#fbfbfb"/>
        <stop offset="1" stop-color="#f0f0f0"/>
      </linearGradient>
      <linearGradient id="grass" x1="0" y1="0" x2="0" y2="1">
        <stop offset="0" stop-color="#b54a4f"/>
        <stop offset="0.35" stop-color="#4f9a2e"/>
        <stop offset="1" stop-color="#3d7d24"/>
      </linearGradient>
      <linearGradient id="couch" x1="0" y1="0" x2="1" y2="1">
        <stop offset="0" stop-color="#e4e6ea"/>
        <stop offset="0.6" stop-color="#3a3d45"/>
        <stop offset="1" stop-color="#d8d9dc"/>
      </linearGradient>
      <linearGradient id="pups" x1="0" y1="0" x2="0" y2="1">
        <stop offset="0" stop-color="#2f4a22"/>
        <stop offset="1" stop-color="#c89a5c"/>
      </linearGradient>
      <linearGradient id="woods" x1="0" y1="0" x2="1" y2="1">
        <stop offset="0" stop-color="#6d5a4c"/>
        <stop offset="0.5" stop-color="#e6ddc9"/>
        <stop offset="1" stop-color="#7c7063"/>
      </linearGradient>
      <clipPath id="art1"><rect x="0" y="0" width="635" height="201"/></clipPath>
    </defs>
    <rect class="cover-paper" width="635" height="242" fill="url(#paper1)"/>

    <g clip-path="url(#art1)">
      <polygon role="img" aria-label="Golden retriever sitting on a lawn lined with small flags" points="430,-75 525,20 430,115 335,20" fill="url(#grass)"/>
      <polygon role="img" aria-label="Black cane corso lying on a white sofa" points="335,50 410,125 335,200 260,125" fill="url(#couch)"/>
      <polygon role="img" aria-label="Three golden retriever puppies looking up" points="430,143 515,228 430,313 345,228" fill="url(#pups)"/>
      <polygon role="img" aria-label="Yellow labrador sitting on a tree stump in autumn woods" points="532,0 635,0 635,201 520,201 448,130 522,56 540,0" fill="url(#woods)"/>
      <polygon points="430,118 444,132 430,146 416,132" fill="#1a1a1a"/>
    </g>

    <g class="brand">
      <circle cx="128" cy="45" r="24" fill="var(--navy)"/>
      <text class="brand-name" x="128" y="98" text-anchor="middle">FURLOW PAWS</text>
    </g>

    <text class="headline-top" x="17" y="150" textLength="236" lengthAdjust="spacingAndGlyphs">WORLD RENOWNED</text>
    <text class="headline-main" x="17" y="188" textLength="231" lengthAdjust="spacingAndGlyphs">DOG TRAINING</text>

    <g class="contact-band">
      <polygon points="0,201 170,201 150,242 0,242" fill="var(--red)"/>
      <polygon points="176,201 635,201 635,242 156,242" fill="var(--navy)"/>
      <text class="band-offer" x="19" y="218">FREE CONSULT</text>
      <rect x="190" y="209" width="12" height="23" rx="2.5" fill="none" stroke="var(--red)" stroke-width="2.5"/>
      <text class="band-phone" x="211" y="232" textLength="174" lengthAdjust="spacingAndGlyphs">410-587-3920</text>
      <g fill="none" stroke="var(--red)" stroke-width="1.6">
        <circle cx="405" cy="222" r="8"/>
        <ellipse cx="405" cy="222" rx="3.5" ry="8"/>
        <line x1="397" y1="222" x2="413" y2="222"/>
        <line x1="399" y1="217" x2="411" y2="217"/>
        <line x1="399" y1="227" x2="411" y2="227"/>
      </g>
      <text class="band-web" x="421" y="228" textLength="197" lengthAdjust="spacingAndGlyphs">WWW.FURLOWPAWS.COM</text>
    </g>
  </svg>

  <p class="sample-label" style="top:674px;">SAMPLE 2</p>
  <p class="sample-size" style="top:674px;">820X312</p>

  <svg class="cover" style="top:771px;" viewBox="0 0 635 242" xmlns="http://www.w3.org/2000/svg">
    <defs>
      <linearGradient id="paper2" x1="0" y1="0" x2="1" y2="1">
        <stop offset="0" stop-color="#e9e9e9"/>
        <stop offset="0.5" stop-color="#fbfbfb"/>
        <stop offset="1" stop-color="#d9d9d9"/>
      </linearGradient>
      <linearGradient id="pupsWide" x1="0" y1="0" x2="0" y2="1">
        <stop offset="0" stop-color="#1f3a1c"/>
        <stop offset="0.45" stop-color="#d9b37a"/>
        <stop offset="1" stop-color="#9a6a3a"/>
      </linearGradient>
      <clipPath id="art2"><rect x="0" y="0" width="635" height="201"/></clipPath>
    </defs>
    <rect class="cover-paper" width="635" height="242" fill="url(#paper2)"/>

    <g clip-path="url(#art2)">
      <ellipse cx="498" cy="82" rx="218" ry="133" fill="var(--red)"/>
      <ellipse cx="504" cy="80" rx="210" ry="128" fill="var(--white)"/>
      <ellipse cx="510" cy="74" rx="206" ry="126" fill="var(--navy)"/>
      <ellipse role="img" aria-label="Three golden retriever puppies resting paws on a wooden rail" cx="520" cy="72" rx="200" ry="122" fill="url(#pupsWide)"/>
    </g>

    <g class="brand">
      <circle cx="128" cy="45" r="24" fill="var(--navy)"/>
      <text class="brand-name" x="128" y="98" text-anchor="middle">FURLOW PAWS</text>
    </g>

    <text class="headline-top" x="17" y="150" textLength="236" lengthAdjust="spacingAndGlyphs">WORLD RENOWNED</text>
    <text class="headline-main" x="17" y="188" textLength="231" lengthAdjust="spacingAndGlyphs">DOG TRAINING</text>

    <g class="contact-band">
      <polygon points="0,201 170,201 150,242 0,242" fill="var(--red)"/>
      <polygon points="176,201 635,201 635,242 156,242" fill="var(--navy)"/>
      <text class="band-offer" x="19" y="218">FREE CONSULT</text>
      <rect x="190" y="209" width="12" height="23" rx="2.5" fill="none" stroke="var(--red)" stroke-width="2.5"/>
      <text class="band-phone" x="211" y="232" textLength="174" lengthAdjust="spacingAndGlyphs">410-587-3920</text>
      <g fill="none" stroke="var(--red)" stroke-width="1.6">
        <circle cx="405" cy="222" r="8"/>
        <ellipse cx="405" cy="222" rx="3.5" ry="8"/>
        <line x1="397" y1="222" x2="413" y2="222"/>
        <line x1="399" y1="217" x2="411" y2="217"/>
        <line x1="399" y1="227" x2="411" y2="227"/>
      </g>
      <text class="band-web" x="421" y="228" textLength="197" lengthAdjust="spacingAndGlyphs">WWW.FURLOWPAWS.COM</text>
    </g>
  </svg>
</main>
</body>
</html>
```